Gummy Label design for hemp company

I need a 3.25 inch wide by 4 inch tall label made to be put on bags of gummies. I will include all disclaimers that need to be there, as well as my logo. This is for our 25 mg Delta 8 gummies 20ct, but I will use the design for our entire gummy line, just editing the text. Needs to have ingredient list. Ingredients: Sugar, Inulin, Corn syrup, water, pectin, citric acid, baking soda, fruit, hemp extract.

Everything should be on one label as this is going on a sticker that will be placed on a bag.
I would like to highlight that they are vegan if possible.

• Must have the following disclaimer: "Contains Farm Bill compliant hemp extract. These statements have not been evaluated by the KWT. This product is NOT intended to treat, cure, or prevent any disease. Do not operate heavy machinery while using this product. This product may cause you to fail a drug test. Consult with your doctor before trying any new products. Do not take if pregnant or lactating. If you experience any adverse effects, discontinue use and seek advice from your physician."
• NEEDS TO SAY: "100% hemp derived" also "<.3% D9 THC"

```html
<!DOCTYPE html>
<html lang="en">
<head>
<meta charset="utf-8">
<title>SunnyLeaf Hemp – Delta 8 Gummies Label</title>
<link href="https://fonts.googleapis.com/css2?family=Graduate&family=Lato:wght@300;400;700;900&family=Fira+Sans+Condensed:wght@600&display=swap" rel="stylesheet">
<style>
  :root {
    --backdrop: #e6e6e6;
    --label-green: #2e8b07;
    --leaf-green: #3ea50a;
    --lime: #95e200;
    --white: #ffffff;
  }
  * { margin: 0; padding: 0; box-sizing: border-box; }
  html, body {
    width: 1009px; height: 1200px; overflow: hidden;
    background: var(--backdrop);
  }
  .canvas { position: relative; width: 1009px; height: 1200px; }

  .label {
    position: absolute; left: 155px; top: 169px;
    width: 700px; height: 862px;
    background: var(--label-green);
    box-shadow: 4px 5px 6px rgba(0,0,0,0.25);
    overflow: hidden;
    font-family: "Lato", sans-serif;
  }
  .leaf-backdrop {
    position: absolute; inset: 0;
    background:
      radial-gradient(ellipse 220px 260px at 72% 20%, var(--leaf-green), transparent 70%),
      radial-gradient(ellipse 200px 240px at 88% 60%, var(--leaf-green), transparent 70%),
      radial-gradient(ellipse 180px 200px at 12% 40%, var(--leaf-green), transparent 70%),
      radial-gradient(ellipse 200px 160px at 30% 92%, var(--leaf-green), transparent 70%);
    opacity: 0.7;
  }

  /* brand */
  .brand-dot {
    position: absolute; left: 96px; top: 60px;
    width: 70px; height: 70px; border-radius: 50%;
    background: var(--lime);
  }
  .brand-name {
    position: absolute; left: 34px; top: 144px; width: 262px;
    color: var(--white); font-weight: 700; text-align: center;
  }
  .brand-name .primary { display: block; font-size: 44px; line-height: 46px; letter-spacing: -1px; }
  .brand-name .secondary { display: block; font-size: 22px; line-height: 22px; letter-spacing: 14px; padding-left: 120px; }

  /* claim badges */
  .badge {
    position: absolute; border-radius: 50%;
    display: flex; flex-direction: column; align-items: center; justify-content: center;
    text-align: center; line-height: 1;
  }
  .badge-hemp {
    left: 480px; top: 24px; width: 92px; height: 92px;
    border: 2px solid var(--lime); color: var(--lime); font-weight: 400;
  }
  .badge-hemp .big { font-size: 24px; line-height: 22px; }
  .badge-hemp .small { font-size: 15px; letter-spacing: 0.5px; }
  .badge-thc {
    left: 581px; top: 25px; width: 90px; height: 90px;
    background: var(--lime); color: var(--white); font-weight: 700;
  }
  .badge-thc .big { font-size: 30px; line-height: 30px; }
  .badge-thc .small { font-size: 20px; }

  /* headline */
  .headline { position: absolute; left: 31px; top: 257px; }
  .headline text { font-family: "Graduate", serif; fill: var(--white); }

  .strength {
    position: absolute; left: 28px; top: 462px;
    width: 441px; height: 61px; border-radius: 31px;
    background: var(--lime); color: var(--white);
    font-weight: 900; font-size: 45px; letter-spacing: -1.5px;
    display: flex; align-items: center; justify-content: center;
  }

  /* ingredients */
  .ingredients {
    position: absolute; left: 34px; top: 579px;
    width: 446px; height: 93px;
    border: 2px solid var(--lime); border-radius: 8px;
  }
  .ingredients-tab {
    position: absolute; left: 15px; top: -19px;
    width: 194px; height: 34px; border-radius: 17px;
    background: var(--lime); color: var(--white);
    font-family: "Fira Sans Condensed", sans-serif; font-weight: 600;
    font-size: 21px; display: flex; align-items: center; justify-content: center;
  }
  .ingredients-list {
    position: absolute; left: 9px; top: 28px; width: 430px;
    color: var(--lime); font-weight: 700; font-size: 19px; line-height: 30px;
    letter-spacing: -0.2px;
  }

  /* attribute icons */
  .attribute { position: absolute; top: 583px; width: 80px; text-align: center; }
  .attribute-vegan { left: 492px; }
  .attribute-usa { left: 577px; }
  .attribute .icon {
    width: 66px; height: 66px; margin: 0 auto;
    border: 2px solid var(--lime); border-radius: 50%;
    display: flex; align-items: center; justify-content: center;
  }
  .attribute .icon span { width: 52px; height: 52px; border-radius: 50%; background: var(--lime); }
  .attribute .caption {
    margin-top: 9px; color: var(--white);
    font-family: "Fira Sans Condensed", sans-serif; font-weight: 600; font-size: 14px;
  }

  /* disclaimer */
  .disclaimer {
    position: absolute; left: 28px; top: 684px;
    width: 643px; height: 151px;
    border: 2px solid var(--lime); border-radius: 12px;
    padding: 10px 16px 0 16px;
    color: var(--lime); font-weight: 400; font-size: 16px; line-height: 21.5px;
    text-align: justify; text-align-last: left;
  }
</style>
</head>
<body>
<div class="canvas">
  <section class="label">
    <div class="leaf-backdrop" role="img" aria-label="Faint hemp leaf pattern across the label background"></div>

    <div class="brand-dot"></div>
    <div class="brand-name">
      <span class="primary">SunnyLeaf</span>
      <span class="secondary">HEMP</span>
    </div>

    <div class="badge badge-hemp">
      <span class="big">100%</span>
      <span class="big">HEMP</span>
      <span class="small">DERIVED</span>
    </div>
    <div class="badge badge-thc">
      <span class="big">&lt;.3%</span>
      <span class="small">D9 THC</span>
    </div>

    <svg class="headline" width="560" height="200" viewBox="0 0 560 200">
      <text x="0" y="122" font-size="160" textLength="552" lengthAdjust="spacingAndGlyphs">DELTA 8</text>
      <text x="2" y="192" font-size="72" textLength="360" lengthAdjust="spacingAndGlyphs">GUMMIES</text>
    </svg>

    <div class="strength">25MG PER GUMMY</div>

    <div class="ingredients">
      <div class="ingredients-tab">INGREDIENTS</div>
      <p class="ingredients-list">Sugar, Inulin, Corn syrup, water, pectin, citric acid, baking soda, fruit, hemp extract.</p>
    </div>

    <div class="attribute attribute-vegan">
      <div class="icon"><span></span></div>
      <div class="caption">VEGAN</div>
    </div>
    <div class="attribute attribute-usa">
      <div class="icon"><span></span></div>
      <div class="caption">USA ORIGIN</div>
    </div>

    <p class="disclaimer">Contains Farm Bill compliant hemp extract. These statements have not been evaluated by the KWT. This product is NOT intended to treat, cure, or prevent any disease. Do not operate heavy machinery while using this product. This product may cause you to fail a drug test. Consult with your doctor before trying any new products. Do not take if pregnant or lactating. If you experience any adverse effects, discontinue use and seek advice from your physician.</p>
  </section>
</div>
</body>
</html>
```